Business Card Design Project for Web Development Company

Need a professional card that stands out with both color and texture.
We provide websites and web development services for small businesses with a focus on connections. Examples include: Automotive repair shop, we take their repair logs and make them available online so their customers can view, print and share (when selling) their maintenance records. Vet clinic, we create systems where customers can sign up for a recurring payment program for the annual wellness checks on their pets and get reminders when it's time, then see and schedule their own appointments. Etc... So not simply a website, but one that connects systems or customers to the business.
Important - !!!!We will be using http://brightinkpress.example/ for the cards, so take a look at what options are available for business card printing, they can do a lot of cool things!!!!
You can pick any 1-3 options from brightinkpress. I'm leaning towards a black background, but the logo will work on any color.
Front:
Martin Keller
2750 SW 8th Ave STE 204-187
Salem, OR 97302
541-555-0172 - cell
541-555-0138 - office
martin@sitelinkhub.example
www.SiteLinkHub.example
Updates
We provide websites and web development services for small businesses with a focus on connections. Examples include: Automotive repair shop, we take their repair logs and make them available online so their customers can view, print and share (when selling) their maintenance records. Vet clinic, we create systems where customers can sign up for a recurring payment program for the annual wellness checks on their pets and get reminders when it''s time, then see and schedule their own appointments. Etc... So not simply a website, but one that connects systems or customers to the business.
Target Market(s)
Small business owners
Industry/Entity Type
Automotive
Look and feel

```html
<!DOCTYPE html>
<html lang="en">
<head>
<meta charset="utf-8">
<title>SiteLinkHub Business Card</title>
<link href="https://fonts.googleapis.com/css2?family=Arimo:wght@400;700&family=Roboto+Condensed:wght@400;500&display=swap" rel="stylesheet">
<style>
  :root {
    --page: #d9dfdd;
    --card: #eef1f0;
    --card-edge: #c9d1ce;
    --nav: #b9c4c0;
    --ink: #1f2a30;
    --blue: #3bb4f2;
    --row-top: #ffffff;
    --row-bottom: #d6d9d8;
    --divider: #c3c9c7;
  }
  * { box-sizing: border-box; margin: 0; padding: 0; }
  html, body { width: 1200px; height: 1200px; overflow: hidden; }
  body {
    background: var(--page);
    font-family: "Arimo", Arial, sans-serif;
    color: var(--ink);
    display: flex;
    flex-direction: column;
    align-items: center;
    justify-content: center;
    gap: 60px;
  }
  .card {
    width: 760px;
    height: 484px;
    border-radius: 14px;
    border: 1px solid var(--card-edge);
    background: var(--card);
    overflow: hidden;
  }
  /* Front */
  .card-front { display: flex; flex-direction: column; }
  .profile {
    height: 165px;
    display: flex;
    align-items: center;
    padding: 0 28px 0 24px;
    background: linear-gradient(#f4f6f5, #e6eae9);
  }
  .portrait {
    width: 134px; height: 118px;
    border: 4px solid #b9c6c1;
    background: linear-gradient(#e3e9e6, #cfd8d4);
    flex: none;
  }
  .identity { margin-left: 18px; flex: 1; font-family: "Roboto Condensed", sans-serif; }
  .identity .name { font-size: 30px; font-weight: 500; }
  .identity .role { font-size: 27px; margin-top: 16px; }
  .contact-art {
    width: 176px; height: 120px;
    border-radius: 10px;
    background: linear-gradient(#f7f8f8, #d4d9d8);
    flex: none;
  }
  .nav {
    height: 46px;
    background: var(--nav);
    display: flex;
    align-items: center;
    padding: 0 12px 0 28px;
    font-size: 26px;
    font-weight: 700;
  }
  .nav span { margin-right: 30px; }
  .search {
    margin-left: auto;
    width: 198px; height: 34px;
    background: #fff;
    border: 1px solid #a9b3b0;
    font-size: 18px; font-weight: 400;
    display: flex; align-items: center; justify-content: flex-end;
    padding-right: 12px;
  }
  .details {
    flex: 1;
    display: grid;
    grid-template-columns: 378px 1fr;
    grid-template-rows: repeat(3, 1fr);
  }
  .item {
    display: flex; align-items: center;
    background: linear-gradient(var(--row-top), var(--row-bottom));
    border-bottom: 2px solid var(--divider);
    padding-left: 22px;
    font-size: 20px;
    line-height: 1.25;
  }
  .item:nth-child(odd) { border-right: 2px solid var(--divider); }
  .item svg { width: 56px; height: 56px; flex: none; margin-right: 22px; }
  .wordmark {
    font-family: "Arimo", Arial, sans-serif;
    font-weight: 700;
    color: var(--blue);
    letter-spacing: 1px;
  }
  .item .wordmark { font-size: 40px; margin-left: 18px; }
  /* Back */
  .card-back {
    display: flex; flex-direction: column;
    align-items: center; justify-content: center;
    gap: 34px;
    background: linear-gradient(#eef2f1, #dfe6e4);
  }
  .globe {
    width: 190px; height: 190px; border-radius: 50%;
    background: radial-gradient(circle at 35% 30%, #7fd0f7, #2f8fd0 60%, #4e5a60);
  }
  .card-back .wordmark { font-size: 78px; }
</style>
</head>
<body>
  <section class="card card-front">
    <header class="profile">
      <div class="portrait" role="img" aria-label="Portrait photo placeholder"></div>
      <div class="identity">
        <p class="name">Martin Keller</p>
        <p class="role">Web Designer / Developer</p>
      </div>
      <div class="contact-art" role="img" aria-label="Illustration of stacked contact cards"></div>
    </header>
    <nav class="nav">
      <span>About</span><span>Portofolio</span><span>Links</span><span>Networks</span>
      <div class="search">Search</div>
    </nav>
    <div class="details">
      <div class="item">
        <svg viewBox="0 0 56 56"><path d="M6 28 L28 8 L50 28" fill="none" stroke="#3a9fd6" stroke-width="5" stroke-linejoin="round"/><rect x="13" y="27" width="30" height="23" fill="#e9eef0" stroke="#8d9aa0" stroke-width="2"/><rect x="24" y="36" width="9" height="14" fill="#3a9fd6"/></svg>
        <p>2750 SW 8th Ave STE 204-187<br>Salem, OR 97302</p>
      </div>
      <div class="item">
        <svg viewBox="0 0 56 56"><rect x="5" y="14" width="46" height="32" rx="3" fill="#f3f5f6" stroke="#8d9aa0" stroke-width="2"/><path d="M5 16 L28 34 L51 16" fill="none" stroke="#8d9aa0" stroke-width="2"/><rect x="16" y="6" width="24" height="12" fill="#3bb4f2"/></svg>
        <p>martin@sitelinkhub.example</p>
      </div>
      <div class="item">
        <svg viewBox="0 0 56 56"><rect x="15" y="3" width="26" height="50" rx="5" fill="#1c2226"/><rect x="18" y="10" width="20" height="34" fill="#3bb4f2"/><circle cx="28" cy="48" r="2.5" fill="#59636a"/></svg>
        <p>Cell - 541-555-0172</p>
      </div>
      <div class="item">
        <svg viewBox="0 0 56 56"><circle cx="28" cy="28" r="24" fill="#3b8fcf"/><circle cx="28" cy="28" r="24" fill="none" stroke="#4e5a60" stroke-width="2"/></svg>
        <p>www.SiteLinkHub.example</p>
      </div>
      <div class="item">
        <svg viewBox="0 0 56 56"><circle cx="28" cy="28" r="25" fill="#45aee8"/><path d="M20 14 C14 20 16 34 26 42 C30 45 35 45 37 43 L33 37 L29 39 C24 35 22 29 23 24 L27 22 L24 15 Z" fill="#fff"/></svg>
        <p>Office - 541-555-0138</p>
      </div>
      <div class="item">
        <span class="wordmark">SiteLinkHub</span>
      </div>
    </div>
  </section>

  <section class="card card-back">
    <div class="globe" role="img" aria-label="Illustration of a globe"></div>
    <span class="wordmark">SiteLinkHub</span>
  </section>
</body>
</html>
```